Private Optometric Practice Needs new Presentation Folders/Stationary

We recently moved our office and are looking to refresh our presentation folders and stationary. I tend to prefer simple, clean designs. We are a full scope optometric practice provide high quality eyewear, custom contact lenses, along with emergency care and treatment for dry eyes. We communicate with a lot of other doctors and want to exude professionalism. I have attached 2 versions of our logo.

Target Market(s)

Familys

Industry/Entity Type

Eyecare

Font styles to use
Sans Serif

Colors
0054AA
0677BA
7BADD7
CADEEF
E8F1F8

Requirements
Nice to have
• Bifold, areas to put information about practice, welcome letter

```html
<!DOCTYPE html>
<html lang="en">
<head>
<meta charset="utf-8">
<title>Norvale Eyecare Stationery</title>
<link href="https://fonts.googleapis.com/css2?family=Montserrat:wght@300;400;700&family=Barlow+Condensed:wght@500&display=swap" rel="stylesheet">
<style>
:root{
  --bg:#ececec;
  --paper:#f4f4f4;
  --white:#ffffff;
  --blue:#1f8fcd;
  --blue-deep:#0677ba;
  --blue-soft:#42a6d6;
  --ink:#111316;
  --slate:#4a4d57;
  --navy:#0b2a4e;
}
*{margin:0;padding:0;box-sizing:border-box}
html,body{width:1200px;height:857px;overflow:hidden;background:var(--bg);font-family:"Montserrat",sans-serif;color:var(--ink)}
.canvas{position:relative;width:1200px;height:857px}
.piece{position:absolute;box-shadow:0 2px 6px rgba(0,0,0,.12)}
.wordmark{font-weight:300;letter-spacing:.22em;text-align:center;line-height:1}
.wordmark .sub{display:block;font-weight:400;letter-spacing:.9em;margin-top:.45em}
.dot{border-radius:50%;background:var(--blue);margin:0 auto}

/* Letterhead */
.letterhead{left:247px;top:82px;width:357px;height:503px;background:var(--paper)}
.letterhead .dot{position:absolute;left:163px;top:12px;width:30px;height:30px}
.letterhead .band{position:absolute;top:49px;height:16px}
.letterhead .band.left{left:0;width:115px}
.letterhead .band.right{left:243px;right:0}
.band i{display:block;height:6px;background:var(--blue)}
.band b{display:block;height:6px;margin-top:4px;background:var(--ink)}
.letterhead .wordmark{position:absolute;left:115px;width:128px;top:53px;font-size:16px;color:var(--ink)}
.letterhead .wordmark .sub{font-size:5px}
.lh-contact{position:absolute;left:18px;right:18px;top:456px;display:flex;justify-content:space-between;align-items:center;font-size:7px}
.lh-contact span{display:flex;align-items:center;gap:5px}
.ico{width:11px;height:11px;background:var(--ink);display:inline-flex;align-items:center;justify-content:center}
.ico.blue{background:var(--blue)}
.lh-pill{position:absolute;left:67px;width:223px;top:476px;height:10px;background:var(--blue);border-radius:6px 6px 0 0}
.lh-foot{position:absolute;left:0;right:0;bottom:0;height:18px;background:var(--ink)}

/* Folder */
.folder{left:625px;top:53px;width:391px;height:533px;background:linear-gradient(160deg,var(--blue) 0%,#2593cf 50%,#1c86c2 100%)}
.folder .flap{position:absolute;left:337px;top:0;bottom:0;width:2px;background:rgba(0,0,0,.18)}
.folder .dot{position:absolute;left:130px;top:180px;width:60px;height:60px;background:var(--white)}
.folder .wordmark{position:absolute;left:0;width:337px;top:278px;font-size:40px;color:#e9f1f8}
.folder .wordmark .sub{font-size:12px;font-weight:700}

/* Vertical card */
.slim-card{left:1027px;top:198px;width:130px;height:461px;background:var(--white);overflow:hidden}
.slim-card .edge{position:absolute;left:0;top:0;bottom:0;width:12px;background:var(--slate)}
.slim-card .bar{position:absolute;left:7px;top:8px;width:10px;height:280px;background:var(--blue);border-radius:5px}
.slim-inner{position:absolute;left:130px;top:0;width:461px;height:130px;transform-origin:0 0;transform:rotate(90deg)}
.slim-inner .dot{position:absolute;left:65px;top:10px;width:42px;height:42px;margin:0}
.slim-inner .wordmark{position:absolute;left:30px;top:62px;font-size:26px;text-align:left}
.slim-inner .wordmark .sub{font-size:6px;letter-spacing:1.4em}
.slim-inner .rule{position:absolute;left:212px;top:12px;width:1.5px;height:96px;background:var(--ink)}
.slim-name{position:absolute;left:226px;top:13px;font-weight:700;font-size:12px;letter-spacing:.03em}
.slim-lines{position:absolute;left:226px;top:38px;font-size:9.5px;line-height:1.45}

/* Business cards */
.card-front{left:87px;top:614px;width:139px;height:87px;background:var(--white);overflow:hidden}
.card-front .photo{position:absolute;left:0;bottom:0;width:66px;height:56px;background:linear-gradient(135deg,#d9dde2,#a9b8c8 60%,#7f9fc0)}
.card-front .stripe{position:absolute;left:65px;top:0;bottom:0;width:3px;background:var(--blue)}
.card-front .dot{position:absolute;left:26px;top:6px;width:11px;height:11px;margin:0}
.card-front .wordmark{position:absolute;left:2px;width:60px;top:20px;font-size:6.5px;color:var(--slate)}
.card-front .wordmark .sub{font-size:2.5px}
.cf-name{position:absolute;left:72px;top:12px;font-weight:700;font-size:6.5px;color:var(--blue-deep);line-height:1.2}
.cf-lines{position:absolute;left:72px;top:40px;font-size:3.6px;line-height:2.1;color:var(--ink)}
.card-back{left:87px;top:714px;width:139px;height:86px;overflow:hidden}
.card-back .photo{position:absolute;inset:0;background:radial-gradient(circle at 65% 25%,#3e6d93,#163a63 55%,var(--navy))}
.card-back .wordmark{position:absolute;left:0;width:139px;top:52px;font-size:10px;color:#dfe8f1}
.card-back .wordmark .sub{font-size:3.5px}
.card-back .dot{position:absolute;left:58px;top:20px;width:22px;height:22px}

/* White envelope */
.envelope{left:248px;top:611px;width:374px;height:189px;background:var(--paper);overflow:hidden}
.envelope .dot{position:absolute;left:24px;top:12px;width:30px;height:30px;margin:0}
.envelope .wordmark{position:absolute;left:8px;width:76px;top:46px;font-size:13px;color:var(--ink)}
.envelope .wordmark .sub{font-size:4.5px}
.env-lines{position:absolute;left:9px;top:143px;font-family:"Barlow Condensed",sans-serif;font-size:6.5px;line-height:1.45}
.env-lines span{display:flex;align-items:center;gap:4px}
.env-bands{position:absolute;left:0;bottom:0}

/* Blue envelope */
.env-blue{left:638px;top:610px;width:372px;height:187px;background:linear-gradient(180deg,var(--blue-soft),#48abd1)}
.env-blue .flap{position:absolute;left:0;right:0;top:0;height:52px;background:#2993cf;border-radius:0 0 5px 5px}
.env-blue .dot{position:absolute;left:163px;top:70px;width:44px;height:44px;background:#e4edf4}
.env-blue .wordmark{position:absolute;left:0;width:372px;top:130px;font-size:20px;color:#e4edf4}
.env-blue .wordmark .sub{font-size:6px;font-weight:700}
</style>
</head>
<body>
<main class="canvas">

  <section class="piece letterhead" aria-label="Letterhead">
    <div class="dot"></div>
    <div class="band left"><i></i><b></b></div>
    <div class="band right"><i></i><b></b></div>
    <div class="wordmark">NORVALE<span class="sub">EYECARE</span></div>
    <div class="lh-contact">
      <span><span class="ico"><svg width="7" height="7" viewBox="0 0 10 10"><path d="M2 1l2 2-1 1.5a6 6 0 0 0 2.5 2.5L7 6l2 2-1.5 1.5C4 9 1 6 .5 2.5z" fill="#fff"/></svg></span>555-014-2290</span>
      <span><span class="ico blue"><svg width="7" height="7" viewBox="0 0 10 10"><circle cx="5" cy="5" r="4" fill="none" stroke="#fff"/><path d="M1 5h8M5 1v8" stroke="#fff"/></svg></span>www.norvaleeyecare.com</span>
      <span><span class="ico"><svg width="7" height="7" viewBox="0 0 10 10"><path d="M5 9S1.5 5.5 1.5 3.5a3.5 3.5 0 0 1 7 0C8.5 5.5 5 9 5 9z" fill="#fff"/></svg></span>1420 Lakeview Dr.<br>Suite B, Brookfield, WI 53005</span>
    </div>
    <div class="lh-pill"></div>
    <div class="lh-foot"></div>
  </section>

  <section class="piece folder" aria-label="Presentation folder">
    <div class="flap"></div>
    <div class="dot"></div>
    <div class="wordmark">NORVALE<span class="sub">EYECARE</span></div>
  </section>

  <section class="piece slim-card" aria-label="Vertical business card">
    <div class="edge"></div>
    <div class="bar"></div>
    <div class="slim-inner">
      <div class="dot"></div>
      <div class="wordmark">NORVALE<span class="sub">EYECARE</span></div>
      <div class="rule"></div>
      <div class="slim-name">DANIEL WHITFORD, O.D.</div>
      <div class="slim-lines">555-014-2290<br>www.norvaleeyecare.com<br>1420 Lakeview Dr.<br>Suite B, Brookfield, WI 53005</div>
    </div>
  </section>

  <section class="piece card-front" aria-label="Business card front">
    <div class="photo" role="img" aria-label="Photo of an eye exam in progress"></div>
    <div class="stripe"></div>
    <div class="dot"></div>
    <div class="wordmark">NORVALE<span class="sub">EYECARE</span></div>
    <div class="cf-name">DANIEL<br>WHITFORD, O.D.</div>
    <div class="cf-lines">555-014-2290<br>www.norvaleeyecare.com<br>1420 Lakeview Dr.<br>Suite B, Brookfield, WI 53005</div>
  </section>

  <section class="piece card-back" aria-label="Business card back">
    <div class="photo" role="img" aria-label="Close-up photo of an eye in blue tones"></div>
    <div class="dot"></div>
    <div class="wordmark">NORVALE<span class="sub">EYECARE</span></div>
  </section>

  <section class="piece envelope" aria-label="Envelope">
    <div class="dot"></div>
    <div class="wordmark">NORVALE<span class="sub">EYECARE</span></div>
    <div class="env-lines">
      <span><svg width="6" height="6" viewBox="0 0 10 10"><path d="M2 1l2 2-1 1.5a6 6 0 0 0 2.5 2.5L7 6l2 2-1.5 1.5C4 9 1 6 .5 2.5z" fill="#1f8fcd"/></svg>555-014-2290</span>
      <span><svg width="6" height="6" viewBox="0 0 10 10"><circle cx="5" cy="5" r="4" fill="none" stroke="#1f8fcd" stroke-width="1.5"/><path d="M1 5h8M5 1v8" stroke="#1f8fcd"/></svg>www.norvaleeyecare.com</span>
      <span><svg width="6" height="6" viewBox="0 0 10 10"><path d="M5 9S1.5 5.5 1.5 3.5a3.5 3.5 0 0 1 7 0C8.5 5.5 5 9 5 9z" fill="#1f8fcd"/></svg>1420 Lakeview Dr. Suite B, Brookfield, WI 53005</span>
    </div>
    <svg class="env-bands" width="374" height="26" viewBox="0 0 374 26">
      <path d="M0 7h152l-6 6H0z" fill="#2b2d33"/>
      <path d="M160 0H374V26H0v-6h146z" fill="#1f8fcd"/>
      <path d="M0 20h146l14-20" fill="none"/>
    </svg>
  </section>

  <section class="piece env-blue" aria-label="Blue envelope">
    <div class="flap"></div>
    <div class="dot"></div>
    <div class="wordmark">NORVALE<span class="sub">EYECARE</span></div>
  </section>

</main>
</body>
</html>
```